Harvest Ledger Partners Web Page

A modern and attractive Home Web Page for my rebranded Company, Harvest Ledger Partners. My existing website from my old brand is www.plumcorbelgroup.NET. I would like an up to date, modern and eye catching Home Web Page. It should entice the viewer to go further and stay on the site.
I will have my professional webmaster utilize this cover page for my redesigned site.

Target Market(s)

Privately held construction equipment rental companies looking to sell or have their business valued

Number of Pages Required

1 page

Font styles to use
Serif
Sans Serif

Colors
2f74b3
fec41b
fefbf7
faa54b
f37122
33a6d7

Requirements
Must have
• Above the fold I want to engage the customer so he stays on the sight. A call to action: "Free confidential conversation to discuss your unique situation and exit strategy or valuation of your business." Something like that in there.

Above the fold have menu and key offerings. Next section to summarize my business (again see plumcorbelgroup.NET for more info) with links to more details back in the site.
"A leading boutique M&A and Valuation advisory firm with over 30 years rental industry specific experience>
Tabs: Seller Representation
Business Valuations
Dependable Advice
Industry Articles
Industry Transactions/News
FAQ
Bottom should have key contact info

Key contact info.
Nice to have
• Logos of associations I belong to (on existing site at plumcorbelgroup.NET) (OTV and PLM only)
"Call Gus today for a free, confidential conversation regarding your unique situation and possible exit strategies."
Should not have
• Too much "busyness"

```html
<!DOCTYPE html>
<html lang="en">
<head>
<meta charset="utf-8">
<title>Harvest Ledger Partners – Home</title>
<link href="https://fonts.googleapis.com/css2?family=Archivo:wght@700;800;900&family=Montserrat:wght@400;500;600;700&display=swap" rel="stylesheet">
<style>
:root{
  --navy:#124a85;
  --navy-deep:#0e3a6a;
  --ink:#0d2540;
  --orange:#f37122;
  --white:#ffffff;
  --paper:#f3f3f3;
  --text:#1c1c1c;
  --muted:#555;
}
*{box-sizing:border-box;margin:0;padding:0}
html,body{width:1200px;height:3932px;overflow:hidden;background:var(--white)}
body{font-family:"Montserrat",sans-serif;color:var(--text)}
h1,h2,h3,.display{font-family:"Archivo",sans-serif;font-weight:800}
.wrap{width:800px;margin:0 auto;position:relative}
.btn{display:inline-block;background:var(--orange);color:var(--white);font-family:"Archivo",sans-serif;font-weight:800;text-decoration:none}
section{position:relative;overflow:hidden}

.topbar{height:46px;background:var(--orange);color:var(--white);font-size:15px;display:flex;align-items:center;justify-content:center}

.hero{height:520px;background:var(--navy)}
.hero svg{position:absolute;inset:0}
.hero .nav{position:absolute;top:0;left:200px;right:200px;height:56px;display:flex;align-items:center}
.brand{background:var(--white);height:52px;width:126px;display:flex;align-items:center;gap:6px;padding:0 8px;font-size:10px;font-weight:700;color:var(--navy);line-height:1.15}
.brand .dot{width:14px;height:14px;background:var(--orange);flex:none}
.nav ul{list-style:none;display:flex;gap:16px;margin-left:24px;font-size:10px;color:var(--white);font-weight:500}
.hero-copy{position:absolute;left:200px;top:205px;color:var(--white)}
.hero-copy h1{font-size:28px;letter-spacing:.5px}
.hero-copy p{font-size:21px;margin-top:14px;line-height:1.25;font-weight:400}
.hero-copy .btn{margin-top:18px;font-size:18px;padding:14px 24px}

.maximize{height:481px}
.maximize .copy{position:absolute;left:200px;top:100px;width:400px}
.maximize h2{font-size:25px;line-height:1.2}
.maximize p{font-size:11px;line-height:1.6;margin-top:22px;color:#333}
.maximize .call{font-size:14px;margin-top:22px;color:var(--text)}
.maximize .call b{color:var(--orange)}
.maximize svg{position:absolute;left:630px;top:57px}

.principal{height:343px;text-align:center}
.principal h2{font-size:24px;line-height:1.25;padding-top:30px}
.principal .tag{font-size:14px;margin-top:18px}
.services{display:flex;gap:6px;margin-top:50px;justify-content:center}
.service{width:194px;height:132px;background:var(--paper);display:flex;flex-direction:column;align-items:center;justify-content:center;gap:12px;font-size:12px;font-weight:700;line-height:1.3}
.service.active{background:var(--white);box-shadow:0 6px 16px rgba(0,0,0,.18)}

.spacer{height:22px}
.about{height:386px;background:var(--navy)}
.about svg{position:absolute;inset:0}
.about .copy{position:absolute;left:204px;top:38px;width:380px;color:var(--white)}
.about h2{font-size:22px}
.about h3{font-family:"Montserrat",sans-serif;font-weight:500;font-size:15px;margin-top:20px}
.about p{font-size:10.5px;line-height:1.6;margin-top:16px;color:#dde6f2}
.about .btn{margin-top:22px;font-size:14px;padding:9px 28px}

.testimonials{height:413px}
.testimonials h2{font-size:25px;text-align:center;padding-top:54px}
.quotes{display:flex;gap:20px;margin-top:40px}
.quote{width:253px}
.quote .card{position:relative;height:174px;background:var(--white);box-shadow:0 4px 14px rgba(0,0,0,.15);padding:30px 34px;font-size:11px;line-height:1.35}
.quote .card::after{content:"";position:absolute;left:18px;bottom:-14px;border:14px solid transparent;border-bottom:0;border-top-color:var(--white)}
.quote .mark{position:absolute;right:16px;bottom:10px;font-family:"Archivo",sans-serif;font-size:74px;line-height:.6;color:#d5dce6}
.quote .who{display:flex;align-items:center;gap:12px;margin-top:30px;padding-left:14px}
.quote .avatar{width:36px;height:36px;border-radius:50%;background:linear-gradient(#3b4f66,#1a2838)}
.quote .who b{font-family:"Archivo",sans-serif;font-size:13px;display:block}
.quote .who span{font-size:10px}

.callfree{height:375px}
.callfree .art{position:absolute;left:200px;top:0;width:430px;height:375px}
.callfree .copy{position:absolute;left:717px;top:90px}
.callfree h2{font-size:25px}
.callfree p{font-size:20px;line-height:1.25;margin-top:18px}
.callfree .phone{font-family:"Archivo",sans-serif;font-weight:800;color:var(--orange);font-size:27px;margin-top:20px}

.cta{height:207px;background:var(--navy);text-align:center;color:var(--white)}
.cta p{font-family:"Archivo",sans-serif;font-weight:800;font-size:18px;line-height:1.3;padding-top:32px}
.cta .btn{margin-top:20px;font-size:21px;padding:11px 30px}

.articles{height:446px}
.articles h2{font-size:25px;text-align:center;padding-top:60px}
.article-row{display:flex;gap:11px;margin-top:38px}
.article{width:259px}
.article .photo{height:188px}
.article h3{font-family:"Montserrat",sans-serif;font-weight:500;font-size:15px;margin-top:22px}
.article p{font-size:9.5px;line-height:1.4;margin-top:10px;color:#333}
.article a{display:block;font-size:9px;font-weight:700;color:var(--orange);margin-top:12px;text-decoration:none}

.contact{height:494px;background:linear-gradient(180deg,#1b4f8a,#1a548f 60%,#234f80)}
.contact h2{color:var(--white);text-align:center;font-size:25px;padding-top:56px}
.form{margin-top:38px;display:grid;grid-template-columns:repeat(3,1fr);gap:20px 12px}
.field{border:1px solid rgba(255,255,255,.75);height:50px;color:var(--white);font-size:12px;font-weight:600;padding:16px 12px}
.field.wide{grid-column:1/4}
.field.msg{grid-column:1/4;height:132px}
.contact .btn{display:block;width:214px;margin:32px auto 0;text-align:center;font-size:19px;padding:13px 0}

.footer{height:199px;background:var(--ink);color:var(--white)}
.footer .wrap{display:flex;padding-top:56px;font-size:10px}
.footer .col{width:200px}
.footer .col.brandcol{width:160px}
.footer h4{font-size:11px;font-weight:500;margin-bottom:14px}
.fbrand{display:flex;align-items:center;gap:6px;font-weight:700;font-size:10px;line-height:1.2}
.fbrand .dot{width:14px;height:14px;border-radius:50%;background:#e3b24a}
.socials{display:flex;gap:4px;margin:8px 0}
.socials span{width:16px;height:16px;background:var(--white)}
.links{display:grid;grid-template-columns:100px 80px;row-gap:18px}
.info li{list-style:none;display:flex;gap:10px;margin-bottom:12px;line-height:1.4}
.news input{width:200px;height:26px;border:0;font-size:9px;padding:0 8px;font-family:inherit}
.news .btn{font-family:"Montserrat",sans-serif;font-size:9px;font-weight:600;padding:6px 8px;margin-top:10px}
</style>
</head>
<body>

<div class="topbar">Covid's subsiding and the market is heating up! Call us to confidentially discuss your Rental Business!</div>

<section class="hero">
  <svg width="1200" height="520" viewBox="0 0 1200 520">
    <defs>
      <linearGradient id="heroPhoto" x1="0" y1="0" x2="1" y2="1">
        <stop offset="0" stop-color="#c9a37c"/>
        <stop offset=".45" stop-color="#a8864f"/>
        <stop offset=".75" stop-color="#d2a23a"/>
        <stop offset="1" stop-color="#8d7c6a"/>
      </linearGradient>
    </defs>
    <rect x="560" y="0" width="640" height="520" fill="url(#heroPhoto)" role="img" aria-label="Yellow wheel loader on a construction site at sunset"/>
    <polygon points="0,0 577,0 672,520 0,520" fill="var(--navy)"/>
    <polygon points="577,0 597,0 702,520 672,520" fill="var(--orange)"/>
  </svg>
  <div class="nav">
    <div class="brand"><span class="dot"></span>Harvest Ledger Partners</div>
    <ul>
      <li>Seller Representation</li><li>Business Valuations</li><li>Dependable Advice</li><li>Industry Articles</li><li>Industry Transactions/News</li><li>FAQ</li>
    </ul>
  </div>
  <div class="hero-copy">
    <h1>Harvest Ledger Partners.</h1>
    <p>"Your Rental Exit, Planned Well" Seller<br>&nbsp;Representation Business Valuation</p>
    <a class="btn" href="#contact">Contact Now</a>
  </div>
</section>

<section class="maximize">
  <div class="copy">
    <h2>Maximize the Value of Your Rental Company with Harvest Ledger Partners.</h2>
    <p>With our sole focus on the Rental Industry, we will maximize the value of your rental company and provide you with sound, reliable advice. We've sold hundreds of rental locations in 22 years!</p>
    <p>At Corbel Acquisitions LLC, we offer M&amp;A and Valuation Services specifically for equipment and special event rental business owner /operators who are looking for a solid exit strategy.</p>
    <p class="call">For a confidential consultation, call Gus Tallowmere at <b>(555) 014-2290</b> or <b>email Gus.</b></p>
  </div>
  <svg width="370" height="389" viewBox="0 0 370 389">
    <defs>
      <linearGradient id="roadPhoto" x1="0" y1="0" x2="0" y2="1">
        <stop offset="0" stop-color="#8fb0cf"/>
        <stop offset=".45" stop-color="#5d7a5a"/>
        <stop offset="1" stop-color="#9a8f80"/>
      </linearGradient>
    </defs>
    <polygon points="0,389 94,0 370,0 370,389" fill="var(--orange)"/>
    <polygon points="20,389 104,0 370,0 370,389" fill="url(#roadPhoto)" role="img" aria-label="Road crew in safety vests working beside a paving machine"/>
  </svg>
</section>

<section class="principal">
  <div class="wrap">
    <h2>Harvest Ledger Partners.Gus<br>Tallowmere Principal</h2>
    <p class="tag">'The Leading M&amp;A Firm in the Rental Industry Today'</p>
    <div class="services">
      <div class="service">
        <svg width="34" height="30" viewBox="0 0 34 30"><rect x="2" y="8" width="30" height="20" rx="2" fill="#111"/><rect x="12" y="2" width="10" height="7" fill="none" stroke="#111" stroke-width="3"/><rect x="2" y="15" width="30" height="2" fill="#fff"/></svg>
        Business Sale<br>Representation
      </div>
      <div class="service active">
        <svg width="34" height="34" viewBox="0 0 34 34" fill="none" stroke="#111" stroke-width="2.4"><path d="M6 4l10 12M12 4l-6 6v8"/><rect x="14" y="16" width="14" height="10"/><circle cx="17" cy="29" r="3"/><circle cx="26" cy="29" r="3"/></svg>
        Equipment<br>Rentals
      </div>
      <div class="service">
        <svg width="38" height="30" viewBox="0 0 38 30"><polygon points="19,2 36,28 2,28" fill="#111"/><polygon points="19,14 25,28 13,28" fill="#fff"/></svg>
        Special Event<br>Rentals
      </div>
      <div class="service">
        <svg width="36" height="32" viewBox="0 0 36 32" fill="#111"><rect x="4" y="12" width="8" height="18"/><rect x="14" y="4" width="9" height="26"/><rect x="25" y="14" width="8" height="16"/><rect x="0" y="29" width="36" height="3"/></svg>
        Business<br>Valuations
      </div>
    </div>
  </div>
</section>

<div class="spacer"></div>

<section class="about">
  <svg width="1200" height="386" viewBox="0 0 1200 386">
    <defs>
      <linearGradient id="yardPhoto" x1="0" y1="0" x2="0" y2="1">
        <stop offset="0" stop-color="#a9cdeb"/>
        <stop offset=".5" stop-color="#c9b860"/>
        <stop offset="1" stop-color="#8e8e86"/>
      </linearGradient>
    </defs>
    <polygon points="603,386 689,0 1200,0 1200,386" fill="var(--orange)"/>
    <polygon points="634,386 694,0 1200,0 1200,386" fill="url(#yardPhoto)" role="img" aria-label="Rental yard with yellow excavators lined up behind a fence"/>
  </svg>
  <div class="copy">
    <h2>About Us</h2>
    <h3>Gus J. Tallowmere – Founder and Principal</h3>
    <p>Gus Tallowmere, prior to Co-Founding Harvest Ledger Partners, LLC in July of 2011, was a Co-Founder of Tallowmere, Brisk &amp; Associates (TB&amp;A) in May of 2000. TB&amp;A was the leading Mergers &amp; Acquisitions firm in the equipment and party rental industry prior to its dissolution in June of 2011. Corbel Acquisitions, LLC continues to have the success that Mr. Tallowmere spearheaded with TB&amp;A.</p>
    <p>Prior to owning his own firms, Mr. Tallowmere previously served as Vice-President, Corporate Development for a publicly traded national rental company.</p>
    <a class="btn" href="#about">Read more</a>
  </div>
</section>

<section class="testimonials">
  <div class="wrap">
    <h2>Client Are Saying</h2>
    <div class="quotes">
      <div class="quote">
        <div class="card">Lorem Ipsum is simply dummy text of the printing and typeset ting industry. Lorem Ipsum has been the industry's standard dummy text ever since the 1500s, when an unknown<span class="mark">“</span></div>
        <div class="who"><span class="avatar" role="img" aria-label="Client portrait"></span><div><b>Jon Mercer</b><span>ABC Comapany</span></div></div>
      </div>
      <div class="quote">
        <div class="card">Lorem Ipsum is simply dummy text of the printing and typeset ting industry. Lorem Ipsum has been the industry's standard dummy text ever since the 1500s, when an unknown<span class="mark">“</span></div>
        <div class="who"><span class="avatar" role="img" aria-label="Client portrait"></span><div><b>Jon Mercer</b><span>ABC Comapany</span></div></div>
      </div>
      <div class="quote">
        <div class="card">Lorem Ipsum is simply dummy text of the printing and typeset ting industry. Lorem Ipsum has been the industry's standard dummy text ever since the 1500s, when an unknown<span class="mark">“</span></div>
        <div class="who"><span class="avatar" role="img" aria-label="Client portrait"></span><div><b>Jon Mercer</b><span>ABC Comapany</span></div></div>
      </div>
    </div>
  </div>
</section>

<section class="callfree">
  <div class="art" role="img" aria-label="Worker in a hard hat pointing toward the phone number, beside a scissor lift" style="background:linear-gradient(120deg,#f8d9bf 0%,#e9eef5 45%,#8aa3c4 100%)"></div>
  <div class="copy">
    <h2>Call for a Free</h2>
    <p>Confidential Conversation<br>to discuss your unique<br>situation and needs.</p>
    <div class="phone">555-014-2290</div>
  </div>
</section>

<section class="cta">
  <p>Call Gus today for a free, confidential conversation<br>regarding your unique situation and possible<br>exit strategies</p>
  <a class="btn" href="#contact">Contact Now</a>
</section>

<section class="articles">
  <div class="wrap">
    <h2>Industry Articles</h2>
    <div class="article-row">
      <div class="article">
        <div class="photo" role="img" aria-label="Workers on a concrete formwork site" style="background:linear-gradient(180deg,#9fc3e6,#7d7a5a 70%,#c9b14a)"></div>
        <h3>Fleet Yard Journal</h3>
        <p>It is a long established fact that a reader will be distracted by the readable content of a page</p>
        <a href="#">Read More</a>
      </div>
      <div class="article">
        <div class="photo" role="img" aria-label="Wheel loader moving sand at a dusty site" style="background:linear-gradient(180deg,#e9a24f,#c8743a 60%,#7a4a2a)"></div>
        <h3>Fleet Yard Journal</h3>
        <p>It is a long established fact that a reader will be distracted by the readable content of a page</p>
        <a href="#">Read More</a>
      </div>
      <div class="article">
        <div class="photo" role="img" aria-label="Builder drilling into a brick wall" style="background:linear-gradient(90deg,#b88a6e,#d8d2c8 55%,#5b7580)"></div>
        <h3>Fleet Yard Journal</h3>
        <p>It is a long established fact that a reader will be distracted by the readable content of a page</p>
        <a href="#">Read More</a>
      </div>
    </div>
  </div>
</section>

<section class="contact" id="contact" role="img" aria-label="Contact form over a faded excavator scene in blue">
  <div class="wrap">
    <h2>Contact Us</h2>
    <div class="form">
      <div class="field">Name</div>
      <div class="field">Phone Number</div>
      <div class="field">Subject</div>
      <div class="field wide">Email Id</div>
      <div class="field msg">Message</div>
    </div>
    <a class="btn" href="#">Send Message</a>
  </div>
</section>

<footer class="footer">
  <div class="wrap">
    <div class="col brandcol">
      <div class="fbrand"><span class="dot"></span>Harvest Ledger<br>Partners</div>
      <h4 style="margin:14px 0 0">Fallow Us</h4>
      <div class="socials"><span></span><span></span><span></span><span></span><span></span></div>
      <div style="font-size:9px;line-height:1.4">© 2021 Harvest Ledger<br>Partners</div>
    </div>
    <div class="col">
      <h4>Usefull Link</h4>
      <div class="links"><span>Home</span><span>Aarticle</span><span>About</span><span>News</span><span>Privacy Policy</span><span>Contact Us</span></div>
    </div>
    <div class="col info" style="width:220px">
      <h4>Contact Us</h4>
      <ul>
        <li><svg width="10" height="12" viewBox="0 0 10 12"><path d="M5 0a4 4 0 0 1 4 4c0 3-4 8-4 8S1 7 1 4a4 4 0 0 1 4-4z" fill="#fff"/><circle cx="5" cy="4" r="1.5" fill="#0d2540"/></svg><span>1180 Wrenfield Ct.<br>Alder Springs, CA 95000</span></li>
        <li><svg width="10" height="10" viewBox="0 0 10 10"><path d="M2 0l2 2-1 2a6 6 0 0 0 3 3l2-1 2 2-2 2C4 10 0 6 0 2z" fill="#fff"/></svg><span>555-014-2290</span></li>
        <li><svg width="11" height="8" viewBox="0 0 11 8"><rect x=".5" y=".5" width="10" height="7" fill="none" stroke="#fff"/><path d="M.5.5l5 4 5-4" fill="none" stroke="#fff"/></svg><span>hello@harvestledger.example</span></li>
      </ul>
    </div>
    <div class="col news">
      <h4>Subscribe Our Newsletter</h4>
      <input type="text" placeholder="Enter Your Email Id">
      <br><span class="btn">Subscribe Now</span>
    </div>
  </div>
</footer>

</body>
</html>
```